Business card for Bright Keystone

Front (space for each) - Name, title, qualifications, mobile number, email address, website, name/logo,
Back - Business name/logo and slogan "Your home is our focus" underneath,
in small writing underneath need ABN number, CRN number, ACL number
Target Market(s)
First Home Buyers
Industry/Entity Type
Finance
Contact Information for Business Card
Requirements
Must have
- Front (space for each) - Name, title, qualifications, mobile number, email address, website, name/logo,

```html
<!DOCTYPE html>
<html lang="en">
<head>
<meta charset="utf-8">
<title>Bright Keystone — Business Card</title>
<link href="https://fonts.googleapis.com/css2?family=Montserrat:wght@600;700&family=Open+Sans:wght@400;600&display=swap" rel="stylesheet">
<style>
  :root {
    --page-bg: #2a2a2c;
    --card-bg: #1b1b1c;
    --teal: #12b0a0;
    --green: #7cc544;
    --brand-green: #2fb78a;
    --orange: #f08a3c;
    --white: #ffffff;
    --muted: #e6e6e6;
  }
  * { margin: 0; padding: 0; box-sizing: border-box; }
  html, body { width: 1200px; height: 900px; overflow: hidden; }
  body {
    background: var(--page-bg);
    font-family: "Open Sans", Arial, sans-serif;
    display: flex;
    flex-direction: column;
    align-items: center;
    justify-content: center;
    gap: 48px;
  }
  .card {
    position: relative;
    width: 620px;
    height: 354px;
    background: var(--card-bg);
    box-shadow: 0 14px 30px rgba(0,0,0,0.45);
    overflow: hidden;
  }
  .card__edge {
    position: absolute;
    left: 0; right: 0; bottom: 0;
    height: 6px;
    background: linear-gradient(90deg, var(--teal), var(--green));
  }

  /* Front */
  .card--front { display: flex; align-items: center; padding: 0 48px 0 54px; }
  .brand {
    display: flex;
    align-items: center;
    gap: 14px;
    width: 230px;
  }
  .brand__dot {
    width: 14px; height: 14px; border-radius: 50%;
    background: var(--orange);
    flex: none;
  }
  .brand__name {
    font-family: "Montserrat", Arial, sans-serif;
    font-weight: 700;
    font-size: 30px;
    line-height: 1.05;
    letter-spacing: 2px;
    text-transform: uppercase;
    color: var(--white);
  }
  .divider {
    width: 1px; height: 150px;
    background: var(--brand-green);
    margin: 0 28px 0 18px;
  }
  .person__name {
    font-family: "Montserrat", Arial, sans-serif;
    font-weight: 700;
    font-size: 22px;
    letter-spacing: 1.5px;
    text-transform: uppercase;
    color: var(--brand-green);
  }
  .person__title {
    font-size: 15px;
    color: var(--muted);
    margin: 2px 0 16px;
  }
  .contact { list-style: none; }
  .contact__item {
    display: flex;
    align-items: center;
    gap: 10px;
    font-size: 14px;
    color: var(--muted);
    line-height: 1.75;
  }
  .contact__icon { width: 13px; height: 13px; flex: none; }

  /* Back */
  .card--back {
    display: flex;
    flex-direction: column;
    align-items: center;
    justify-content: center;
    text-align: center;
  }
  .card--back .brand { width: auto; flex-direction: column; gap: 16px; }
  .card--back .brand__name { font-size: 34px; }
  .slogan {
    margin-top: 26px;
    font-family: "Montserrat", Arial, sans-serif;
    font-weight: 700;
    font-size: 17px;
    letter-spacing: 1.5px;
    text-transform: uppercase;
    color: var(--brand-green);
  }
  .registrations {
    margin-top: 8px;
    font-size: 11px;
    letter-spacing: 0.5px;
    color: var(--muted);
    display: flex;
    align-items: center;
    gap: 10px;
  }
  .registrations__sep {
    width: 5px; height: 5px; border-radius: 50%;
    background: var(--orange);
  }
</style>
</head>
<body>

  <section class="card card--front" aria-label="Card front">
    <div class="brand">
      <span class="brand__dot"></span>
      <span class="brand__name">Bright<br>Keystone</span>
    </div>
    <div class="divider"></div>
    <div class="person">
      <h1 class="person__name">Daniel Orwell</h1>
      <p class="person__title">President</p>
      <ul class="contact">
        <li class="contact__item">
          <svg class="contact__icon" viewBox="0 0 24 24" aria-hidden="true"><path fill="var(--orange)" d="M6.6 10.8a15.1 15.1 0 0 0 6.6 6.6l2.2-2.2a1 1 0 0 1 1-.25 11.4 11.4 0 0 0 3.6.57 1 1 0 0 1 1 1V20a1 1 0 0 1-1 1A17 17 0 0 1 3 4a1 1 0 0 1 1-1h3.5a1 1 0 0 1 1 1c0 1.25.2 2.45.57 3.6a1 1 0 0 1-.25 1z"/></svg>
          1300 482 917
        </li>
        <li class="contact__item">
          <svg class="contact__icon" viewBox="0 0 24 24" aria-hidden="true"><path fill="var(--orange)" d="M2 5h20v14H2z"/><path fill="none" stroke="var(--card-bg)" stroke-width="2" d="M2 5l10 8 10-8"/></svg>
          info@brightkeystone.com.au
        </li>
        <li class="contact__item">
          <svg class="contact__icon" viewBox="0 0 24 24" aria-hidden="true"><circle cx="12" cy="12" r="10" fill="var(--orange)"/><path fill="none" stroke="var(--card-bg)" stroke-width="1.5" d="M2 12h20M12 2c3 3 3 17 0 20M12 2c-3 3-3 17 0 20"/></svg>
          www.brightkeystone.com.au
        </li>
      </ul>
    </div>
    <div class="card__edge"></div>
  </section>

  <section class="card card--back" aria-label="Card back">
    <div class="brand">
      <span class="brand__name">Bright Keystone</span>
      <span class="brand__dot"></span>
    </div>
    <p class="slogan">Your home is our focus</p>
    <p class="registrations">
      <span>ABN 62 318 704 915</span>
      <span class="registrations__sep"></span>
      <span>CRN 86420975</span>
      <span class="registrations__sep"></span>
      <span>ACL 604381</span>
    </p>
    <div class="card__edge"></div>
  </section>

</body>
</html>
```